Interactive Children's Media Book Company Website Design

We need a website DESIGN (no coding required) for a new interactive children's media book company called Tovira Studios.

We develop high-quality interactive children's books for the iPad/iPhone that seeks to delight and inspire young and old alike. Our stories are filled with heart and spirit, and we seek to breathe magic back into books so that people fall back in love with reading.

Tovira means "butterfly" in Korean. It plays on the idea that a caterpillar metamorphoses into a butterfly - and in the same way, our readers are transformed through the journey of experiencing our interactive books.

We're looking for something based on the ATTACHED LOGO DESIGN for our company. A website that's professional, modern, fun and inviting; easy to read and not-cluttered, but still portraying the feeling of innocence and childhood.

We're looking for something that resonates the magical experience we want to create for our readers. Specific requirements on pages, tabs, content, etc are below.

Industry/Entity Type

It Company

Requirements
Nice to have
• There are 7 tabs on the Homepage of the website: HOME, GRANDPA, ABOUT US, CAREERS, NEWS, CONTACT US, SHOP. (But there is an extra page called THEIR GARDEN, which will be a sub-page under Grandpa).

HOME
• Would be great to have some key images of our book (3-4 screen shots) as the key focus of the homepage that automatically scroll through every few seconds. (Placeholder image attached). The images would link to the “Grandpa” page.
• Company logo (attached to brief) and slogan: “A new era of children’s media” quite prominent on page.
• Key text content to be on page: “Tovira means “butterfly” in Korean. Just as a caterpillar transforms into a butterfly, Tovira Studios takes the reader on an unforgettable journey of metamorphosis through our stories. We turn children’s books into a high-quality interactive experience on mobile platforms - breathing magic back into books, and inspiring people to fall back in love with reading. Through our unique characters full of heart and spirit, our stories delight and inspire young and old alike.”
• Twitter & Facebook Like & Facebook page link icons.
• Section on Latest News with a few of the latest entries.
• Section on latest sister images & comments that visitors have posted, which takes you to the “Their Garden” page.

GRANDPA
• The title for this page is “Grandpa Keeps a Secret Garden”
• There will be a little iPad/iPhone icon (placeholder attached) for this book.
• There will be a link to the App Store to buy the app book.
• Key text content on this page: “Our debut interactive media book is coming soon on the iPad and iPhone! “Grandpa Keeps a Secret Garden” touches on the beautiful and inextricable (albeit sometimes frustrating!) bond between sisters.”
• There will be a section on “Features” which lists all the various special features the app book includes.
• There will be a YouTube clip embedded into the page, which shows how the app book works.
• A section that says: “Do you have a sister who’s not like other sisters? Share a photo and tell us about her!” which links to the sub-page “Their Garden”.
• Under this, there may be the most recent few images submitted by the public, which when clicked on, would also link to the sub-page “Their Garden”.

THEIR GARDEN
• The main text on the page: “Do you have a sister who’s not like other sisters? Share a photo and tell us about her!”
• Main body of the page is a gallery of all the photos that have been submitted. If you click on each of the images, you get the comments that people have submitted with the photos.
• The page would also have a Submit Comments Form, where people can upload a picture of their sister(s) and write a comment to accompany the image.

ABOUT US
• Introductory text on page: “It was a chance conversation at Harbourview Terminal, where two friends discovered they shared a dream to create quality children's media. Both of them were excited by the possibilities of using new digital platforms to inspire and educate a younger generation. From that idea Tovira Studios was born. We seek to be the chrysalis of story telling - to inspire the hearts and minds of our generation, and generations to come.”
• Section to “Join the Mailing List” where they can put their email address in and submit.
• Bios of 2x people with photos (bios in word doc attached) (do not have photos yet).

CAREERS
• The main text on the page: “We are always on the lookout for talented people to join our team. If you are a writer, illustrator, animator, iOS/android developer, musician, creative-writing translator - or have something special to offer Tovira Studios - we are keen to hear from you. Send us a message through the Contact Us tab above.”

NEWS
• Regular News page, with blog-type entries.

CONTACT US
• Online submit Contact Us form
• The main text on page: “Our studio is based in the Marram Arts Hub, 14 Pellham Street, Ardlow, Wellington. Marram is a professional, creative collective - with four separate studios, gallery, and retail store. For more information on Marram, visit: http://www.marramhub.example.nz”
• “We would love to hear from you! Whether you have questions, ideas, comments, or just want to say hullo - please leave us a message and we will get back to you soon.”
• Including image of the premises (Marram image attached to brief).

SHOP
• Where visitors can purchase merchandise (t-shirts, mugs, etc) of the book/company.

```html
<!DOCTYPE html>
<html lang="en">
<head>
<meta charset="utf-8">
<title>Tovira Studios — A new era of children's media</title>
<link href="https://fonts.googleapis.com/css2?family=Arimo:wght@400;700&family=Comfortaa:wght@400&display=swap" rel="stylesheet">
<style>
  :root {
    --bg-pink: #fbe9f6;
    --bg-lilac: #e9e3fb;
    --bg-cream: #fdf7ec;
    --purple: #7a6cf0;
    --purple-dark: #6a4fe0;
    --nav-top: #a7b3fb;
    --nav-bottom: #9a68ee;
    --text: #3c3c3c;
    --muted: #8a8a8a;
    --brand-grey: #8f8f93;
    --panel: #ffffff;
    --panel-edge: #dcd6ee;
    --thumb: #e6e2e0;
  }
  * { box-sizing: border-box; margin: 0; padding: 0; }
  html, body { width: 1200px; height: 1125px; overflow: hidden; }
  body {
    font-family: "Arimo", Arial, sans-serif;
    color: var(--text);
    background:
      radial-gradient(circle at 6% 40%, var(--bg-cream) 0, transparent 35%),
      radial-gradient(circle at 95% 60%, #efe4fb 0, transparent 40%),
      linear-gradient(180deg, var(--bg-pink) 0%, var(--bg-lilac) 70%, #ece6fb 100%);
    position: relative;
  }
  a { text-decoration: none; }
  .site-header { position: absolute; left: 0; top: 0; width: 1200px; height: 120px; }
  .brand { position: absolute; left: 122px; top: 24px; display: flex; align-items: center; gap: 14px; }
  .brand-mark { width: 62px; height: 62px; border-radius: 50%; background: #a98ff2; flex: none; }
  .brand-name { font-family: "Arimo", Arial, sans-serif; font-weight: 400; font-size: 38px; color: var(--brand-grey); white-space: nowrap; }
  .slogan { position: absolute; left: 457px; top: 30px; font-family: "Comfortaa", sans-serif; font-size: 21px; color: #9a9a9e; letter-spacing: .3px; white-space: nowrap; }
  .social { position: absolute; left: 1022px; top: 29px; display: flex; gap: 6px; }
  .social span { width: 25px; height: 25px; border-radius: 3px; display: block; }
  .social .s1 { background: #4a67a8; }
  .social .s2 { background: #3fb3ea; }
  .main-nav { position: absolute; left: 454px; top: 61px; width: 625px; height: 50px; border-radius: 12px;
    background: linear-gradient(180deg, var(--nav-top) 0%, #9d8cf4 50%, var(--nav-bottom) 100%);
    box-shadow: 0 1px 3px rgba(120,90,200,.35); }
  .main-nav ul { list-style: none; display: flex; align-items: center; justify-content: space-between; height: 100%; padding: 0 17px 0 9px; }
  .main-nav a { display: block; color: #fff; font-weight: 700; font-size: 13.5px; white-space: nowrap; padding: 5px 0; border-radius: 12px; }
  .main-nav .current a { color: #111; background: linear-gradient(180deg, #fff, #e4e4e4); padding: 5px 17px; }
  .hero { position: absolute; left: 120px; top: 133px; width: 960px; height: 645px; border-radius: 14px; overflow: hidden;
    border: 2px solid #fff; box-shadow: 0 0 0 1px var(--panel-edge); }
  .hero-art { width: 100%; height: 100%;
    background: linear-gradient(180deg, #8fd3ef 0%, #b9e6f7 28%, #5a8fd8 42%, #d6a865 60%, #7fb23e 78%, #6f9f35 100%); }
  .hero-arrow { position: absolute; top: 291px; width: 66px; height: 66px; }
  .hero-arrow.prev { left: 14px; }
  .hero-arrow.next { right: 12px; }
  .panel { position: absolute; top: 795px; width: 307px; height: 287px; background: var(--panel); border-radius: 12px;
    border: 1px solid var(--panel-edge); box-shadow: 0 1px 4px rgba(150,130,200,.25); }
  .panel h2 { font-weight: 400; font-size: 24px; color: var(--purple); position: absolute; left: 13px; top: 13px; white-space: nowrap; }
  .welcome { left: 123px; }
  .welcome p { position: absolute; left: 13px; top: 54px; width: 282px; font-size: 11.5px; line-height: 18.8px; color: #454545; }
  .news { left: 447px; }
  .news-list { list-style: none; position: absolute; left: 14px; top: 48px; width: 284px; }
  .news-item { display: flex; gap: 8px; margin-bottom: 9px; }
  .cal { width: 36px; height: 38px; flex: none; border-radius: 3px; background: #f2f2f2; border: 1px solid #c9c9c9; font-size: 9px; line-height: 9px; text-align: center; color: #333; overflow: hidden; }
  .cal .yr { display: block; background: #3ea7e0; color: #fff; padding: 2px 0 1px; margin-bottom: 1px; }
  .news-item h3 { font-size: 11.5px; font-weight: 700; color: #333; margin-bottom: 4px; }
  .news-item p { font-size: 11.5px; line-height: 17px; color: #454545; }
  .news-item p b { color: #222; }
  .community { left: 770px; }
  .post-list { list-style: none; position: absolute; left: 9px; top: 21px; width: 290px; }
  .post { display: flex; gap: 7px; height: 77px; }
  .thumb { width: 84px; height: 66px; flex: none; background: var(--thumb); display: flex; align-items: center; justify-content: center; color: #c8c3c1; font-size: 13px; }
  .thumb span { transform: rotate(-25deg); }
  .post p { font-size: 11.5px; line-height: 17px; color: var(--purple); }
  .post .meta { color: var(--muted); font-size: 10.5px; line-height: 14px; margin-top: 4px; display: flex; align-items: center; gap: 4px; }
  .meta i { width: 13px; height: 12px; border: 1px solid #4a67a8; border-radius: 2px; display: inline-block; }
  .meta em { width: 9px; height: 9px; border-radius: 50%; background: #a9a9a9; display: inline-block; }
  .btn { position: absolute; right: 11px; bottom: 12px; width: 85px; height: 26px; border-radius: 7px; color: #fff; font-size: 11.5px;
    display: flex; align-items: center; justify-content: center;
    background: linear-gradient(180deg, #a995f8, var(--purple-dark)); box-shadow: 0 0 0 2px #cfc6fa; }
  .site-footer { position: absolute; left: 124px; top: 1097px; width: 951px; border-top: 1px solid #8e86a6; text-align: center; font-size: 10.5px; color: #222; padding-top: 8px; }
</style>
</head>
<body>
  <header class="site-header">
    <div class="brand" aria-label="Tovira Studios">
      <span class="brand-mark"></span>
      <span class="brand-name">Tovira Studios</span>
    </div>
    <p class="slogan">A new era of children's media...</p>
    <div class="social">
      <span class="s1" role="img" aria-label="Social page link"></span>
      <span class="s2" role="img" aria-label="Social feed link"></span>
    </div>
    <nav class="main-nav">
      <ul>
        <li class="current"><a href="#home">HOME</a></li>
        <li><a href="#grandpa">GRANDPA</a></li>
        <li><a href="#about">ABOUT US</a></li>
        <li><a href="#careers">CAREERS</a></li>
        <li><a href="#news">NEWS</a></li>
        <li><a href="#contact">CONTACT US</a></li>
        <li><a href="#shop">SHOP</a></li>
      </ul>
    </nav>
  </header>

  <section class="hero">
    <div class="hero-art" role="img" aria-label="Book scene slideshow: a sunny backyard with a trampoline, a blue house, a wooden fence, a red doghouse and a big tree"></div>
    <svg class="hero-arrow prev" viewBox="0 0 66 66" aria-label="Previous slide">
      <circle cx="33" cy="33" r="31" fill="#fff"/><circle cx="33" cy="33" r="22" fill="#333"/>
      <path d="M37 23 L27 33 L37 43" stroke="#fff" stroke-width="5" fill="none" stroke-linecap="round" stroke-linejoin="round"/>
    </svg>
    <svg class="hero-arrow next" viewBox="0 0 66 66" aria-label="Next slide">
      <circle cx="33" cy="33" r="31" fill="#fff"/><circle cx="33" cy="33" r="22" fill="#333"/>
      <path d="M29 23 L39 33 L29 43" stroke="#fff" stroke-width="5" fill="none" stroke-linecap="round" stroke-linejoin="round"/>
    </svg>
  </section>

  <section class="panel welcome">
    <h2>Welcome to tovira</h2>
    <p>Tovira means "butterfly" in Korean. Just as a caterpillar transforms into a butterfly, Tovira Studios takes the reader on an unforgettable journey of metamorphosis through our stories. We turn children's books into a high-quality interactive experience on mobile platforms - breathing magic back into books, and inspiring people to fall back in love with reading. Through our unique characters full of heart and spirit, our stories delight and inspire young and old alike.</p>
    <a class="btn" href="#about">Read More</a>
  </section>

  <section class="panel news">
    <h2>Latest News</h2>
    <ul class="news-list">
      <li class="news-item">
        <div class="cal"><span class="yr">2011</span>Mar<br>24</div>
        <div><h3>News Title 1</h3><p>Lorem ipsum dolor sit amet consecutor. Lorem ipsum dolor sit amet consecutor. <b>More...</b></p></div>
      </li>
      <li class="news-item">
        <div class="cal"><span class="yr">2011</span>Mar<br>24</div>
        <div><h3>News Title 1</h3><p>Lorem ipsum dolor sit amet consecutor. Lorem ipsum dolor sit amet consecutor. Lorem ipsum dolor sit amet consecutor.</p></div>
      </li>
      <li class="news-item">
        <div class="cal"><span class="yr">2011</span>Mar<br>24</div>
        <div><h3>News Title 1</h3><p>Lorem ipsum dolor sit amet consecutor. Lorem ipsum dolor sit amet consecutor. Lorem ipsum dolor sit amet consecutor.</p></div>
      </li>
    </ul>
    <a class="btn" href="#news">Read More</a>
  </section>

  <section class="panel community">
    <ul class="post-list">
      <li class="post">
        <div class="thumb"><span>Thumbnail</span></div>
        <div><p>Lorem ipsum dolor sit amet consecutor. Lorem ipsum dolor sit amet consecutor.</p><div class="meta"><i></i>2 hours ago · <em></em></div></div>
      </li>
      <li class="post">
        <div class="thumb"><span>Thumbnail</span></div>
        <div><p>Lorem ipsum dolor sit amet consecutor. Lorem ipsum dolor sit amet consecutor.</p><div class="meta"><i></i>2 hours ago · <em></em></div></div>
      </li>
      <li class="post">
        <div class="thumb"><span>Thumbnail</span></div>
        <div><p>Lorem ipsum dolor sit amet consecutor. Lorem ipsum dolor sit amet consecutor.</p><div class="meta"><i></i>2 hours ago · <em></em></div></div>
      </li>
    </ul>
    <a class="btn" href="#their-garden">Read More</a>
  </section>

  <footer class="site-footer">Copyright © 2011 tovira. All Rights Reserved</footer>
</body>
</html>
```